New Website for IT Services Business

We need an uncoded web design for a new company based in Australia called "Falcon Tech". We offer specialised point of sale (POS) support to the hospitality industry. We already support hundreds of cafes and restaurants. We are also about to launch and promote a range of new services with the offering of General IT Support being the most important. Other additional services to be offered are Falcon Cloud Backup, reselling and supporting Korvel Antivirus and Tresby Apps.

We have a logo design and our colour scheme is based on the logo with the addition of charcoal grey (see attached logos). We want the pages to reflect precision and efficiency with sharp characteristics. It must be professional but playful/fun elements are encouraged.

Our target audience is restaurant and cafe owners who are interested in finding high quality POS and IT support for their business.

The main call to action on the home page should be either 'Let's Meet For Coffee!' or 'Find out more (by completing a form)'. If you are unsure about what the general text should say then you can use 'Lorem Ipsum' where required.

The site must be viewable at different resolutions and on smart phones and tablets.

The website structure will be quite simple. We require:
- one impressive landing page. Visitors will quickly determine our services and that we provide a very high level of service while also offering value for money. Obviously a clear list of links (however/wherever you like) to the other pages.
- Simple pages with a similar layout for the following:
- Services - "POS & IT Support for the Hospitality Industry" being the main one. With complementary services also listed. Another call to action on this page with the option of 'Let's Meet For Coffee' or a "More information/Pricing" form to be completed by the visitor.
- Products - will be a small online storefront for a few simple products.
- About - Business background. 2x Directors with a photo and brief Bio.
- Downloads - A list of free files to download. Includes remote access client software.
- Contact Us - Mailing address, Email addresses and Support phone number.

Please feel free to ask any questions about the design. I will assist as much as possible.

Thank you for viewing. We promise to give constructive feedback to every person who submits a design. Thank you so much.

Target Market(s)

Restaurant and Cafe owners.

Industry/Entity Type

Hospitality

Requirements
Must have
• - Viewable on different resolutions and on smart phones and tablets.
- Clear call to action of EITHER 'Let's Meet For Coffee' or a "More information/Pricing" form to be completed by the visitor.

```html
<!DOCTYPE html>
<html lang="en">
<head>
<meta charset="utf-8">
<title>Falcon Tech — POS &amp; IT Support</title>
<link href="https://fonts.googleapis.com/css2?family=Oswald:wght@400;500&family=Bebas+Neue&family=Arimo:wght@400;700&display=swap" rel="stylesheet">
<style>
:root{
  --charcoal:#1b1b1d;
  --charcoal-2:#2a2a2d;
  --red:#d41f26;
  --red-dark:#b3161c;
  --silver:#d8d8d8;
  --silver-dark:#a9a9a9;
  --panel:#ececec;
  --ink:#222;
  --text:#333;
  --white:#fff;
}
*{box-sizing:border-box;margin:0;padding:0}
html,body{width:1172px;height:1200px;overflow:hidden}
body{
  position:relative;
  background:radial-gradient(ellipse at 50% 20%,#333336 0%,var(--charcoal) 70%);
  font-family:"Arimo",Arial,sans-serif;color:var(--text);
}
.abs{position:absolute}
.social{display:flex;gap:8px}
.social span{width:28px;height:28px;border-radius:50%;background:#e8e8e8;display:block}
.social-top{left:958px;top:24px}
.site{left:100px;top:72px;width:971px;height:1083px}
.header{left:0;top:0;width:971px;height:96px;border-top:3px solid var(--red);
  background:linear-gradient(#f4f4f4,#c9c9c9)}
.logo-plate{left:-21px;top:11px;width:284px;height:76px}
.logo-name{left:38px;top:10px;display:flex;align-items:center;gap:10px;
  font-family:"Oswald",sans-serif;font-weight:500;font-size:38px;color:var(--ink)}
.logo-name i{width:44px;height:44px;border-radius:50%;background:var(--red);display:block}
.phone{right:12px;top:10px;font-family:"Oswald",sans-serif;font-size:17px;color:#222;display:flex;align-items:center;gap:6px}
.nav{right:0;top:58px;display:flex;font-family:"Oswald",sans-serif;font-size:16px;text-transform:uppercase}
.nav a{text-decoration:none;color:#333;padding:6px 24px 10px;border-left:1px solid #b5b5b5;position:relative}
.nav a:first-child{border-left:0}
.nav a.active{color:var(--red)}
.nav a.active::after{content:"";position:absolute;left:50%;bottom:-1px;margin-left:-6px;
  border:6px solid transparent;border-bottom-color:#fff;border-top:0}
.hero{left:0;top:96px;width:971px;height:434px;
  background:linear-gradient(100deg,#7b6a5c 0%,#a39a8d 30%,#d9d9d6 45%,#5e6a4c 70%,#cfcfcf 100%)}
.hero-copy{right:14px;top:284px;text-align:left;font-family:"Bebas Neue","Oswald",sans-serif;font-weight:400;line-height:.87}
.hero-copy .hl{color:var(--red);font-size:62px;display:block;text-shadow:0 2px 3px rgba(0,0,0,.35)}
.hero-copy .sub{color:#111;font-size:34px;display:block;margin-top:4px}
.arrow{top:268px;width:37px;height:74px;background:#d6d6d6}
.arrow-left{left:-32px;border-radius:37px 0 0 37px}
.arrow-right{right:-32px;border-radius:0 37px 37px 0}
.arrow svg{position:absolute;top:25px}
.cta{left:0;top:530px;width:971px;height:146px;background:linear-gradient(var(--red),var(--red-dark))}
.cta-title{left:8px;top:12px;font-family:"Oswald",sans-serif;font-size:28px;color:#fff;line-height:1.1}
.cta-title span{display:block;padding-left:105px}
.field{background:#f3f3f3;border:1px solid #fff;font-size:10px;color:#444;padding:7px 6px;border-radius:2px}
.submit{left:858px;top:54px;width:90px;height:31px}
.submit b{position:absolute;left:14px;top:2px;font-family:"Oswald",sans-serif;font-weight:400;font-size:19px;color:var(--red)}
.panels{left:0;top:676px;width:971px;height:331px;background:var(--panel)}
.divider{top:35px;width:2px;height:290px;background:linear-gradient(#e0e0e0,#cfcfcf,#e0e0e0)}
.tab{top:-24px;width:240px;height:100px}
.tab h2{position:absolute;left:0;right:0;top:30px;text-align:center;font-family:"Bebas Neue","Oswald",sans-serif;
  font-weight:400;font-size:24px;color:var(--red)}
.icon{width:80px;height:86px;border-radius:12px;background:linear-gradient(#d9d9d9,#bcbcbc)}
.copy{font-size:10.5px;line-height:12.8px;text-align:justify;color:#333}
.copy-lg{font-size:12px;line-height:14.2px;letter-spacing:.2px}
.more{font-size:10px;font-weight:700;color:var(--red);text-decoration:underline}
.rule{height:1px;background:#d2d2d2}
.news h3{font-size:11px;font-weight:700;color:#222;line-height:13px}
.news p{font-size:12px;color:var(--red);margin:5px 0 9px}
.footer{left:0;top:1007px;width:971px;height:76px;background:linear-gradient(var(--red),var(--red-dark));border-radius:0 0 4px 4px}
.footer-nav{left:20px;top:28px;display:flex;font-family:"Oswald",sans-serif;font-size:15px}
.footer-nav a{color:#fff;text-decoration:none;text-transform:uppercase}
.social-foot{right:22px;top:26px}
.copyright{right:108px;top:1170px;font-family:"Oswald",sans-serif;font-size:12px;color:#fff;letter-spacing:-.2px}
.copyright em{font-style:normal;color:var(--red)}
</style>
</head>
<body>

<div class="abs social social-top" aria-label="Social links"><span></span><span></span><span></span></div>

<div class="abs site">
  <header class="abs header">
    <div class="abs phone">
      <svg width="12" height="18" viewBox="0 0 12 18"><path d="M3 1h3l1 4-2 1.5c.6 2 1.6 3.8 3 5.3L10 11l2 3-2 3C5 17 1 10 1 4z" fill="#c8161d"/></svg>
      +123-4610-5930
    </div>
    <nav class="abs nav">
      <a class="active" href="#">Home</a>
      <a href="#">What we are</a>
      <a href="#">What we offer</a>
      <a href="#">Contact us</a>
    </nav>
  </header>

  <div class="abs logo-plate">
    <svg class="abs" width="284" height="88" viewBox="0 0 284 88">
      <polygon points="0,0 246,0 284,38 246,76 0,76" fill="#fff"/>
      <polygon points="0,76 21,76 21,94" fill="#8a8a8a"/>
    </svg>
    <div class="abs logo-name"><i></i>Falcon Tech</div>
  </div>

  <section class="abs hero" role="img" aria-label="Photo of a person using a white laptop at a cafe table beside a coffee cup">
    <div class="abs arrow arrow-left"><svg width="20" height="24" viewBox="0 0 20 24" style="left:10px"><path d="M15 2 5 12l10 10" stroke="#fff" stroke-width="5" fill="none"/></svg></div>
    <div class="abs arrow arrow-right"><svg width="20" height="24" viewBox="0 0 20 24" style="left:6px"><path d="M5 2l10 10L5 22" stroke="#fff" stroke-width="5" fill="none"/></svg></div>
    <h1 class="abs hero-copy">
      <span class="hl">We offer specialised<br>point of sale (POS)</span>
      <span class="sub">Support to the hospitality industry</span>
    </h1>
  </section>

  <section class="abs cta">
    <div class="abs cta-title">'Let's Meet<span>For Coffee'</span></div>
    <svg class="abs" style="left:204px;top:60px" width="80" height="40" viewBox="0 0 80 40">
      <path d="M4 28c16 12 44 8 64-16" stroke="#fff" stroke-width="4" fill="none"/>
      <path d="M58 8l16-2-4 16z" fill="#fff"/>
    </svg>
    <div class="abs field" style="left:306px;top:19px;width:179px;height:28px">Name</div>
    <div class="abs field" style="left:492px;top:19px;width:179px;height:28px">Email</div>
    <div class="abs field" style="left:306px;top:58px;width:179px;height:29px">Contact No.</div>
    <div class="abs field" style="left:492px;top:58px;width:179px;height:29px">Address</div>
    <div class="abs field" style="left:676px;top:18px;width:177px;height:68px;padding-top:5px">Message</div>
    <div class="abs submit">
      <svg width="90" height="31" viewBox="0 0 90 31"><polygon points="0,0 78,0 90,15.5 78,31 0,31" fill="#e6e6e6"/></svg>
      <b>Submit</b>
    </div>
  </section>

  <section class="abs panels">
    <div class="abs divider" style="left:318px"></div>
    <div class="abs divider" style="left:650px"></div>

    <div class="abs tab" style="left:25px">
      <svg width="240" height="100" viewBox="0 0 240 100">
        <polygon points="0,24 19,0 221,0 240,24" fill="#bdbdbd"/>
        <polygon points="19,0 221,0 221,68 120,100 19,68" fill="#d0d0d0"/>
      </svg>
      <h2>Little about Falcon Tech</h2>
    </div>
    <div class="abs tab" style="left:368px">
      <svg width="240" height="100" viewBox="0 0 240 100">
        <polygon points="0,24 19,0 221,0 240,24" fill="#bdbdbd"/>
        <polygon points="19,0 221,0 221,68 120,100 19,68" fill="#d0d0d0"/>
      </svg>
      <h2>What we offer</h2>
    </div>
    <div class="abs tab" style="left:688px">
      <svg width="240" height="100" viewBox="0 0 240 100">
        <polygon points="0,24 19,0 221,0 240,24" fill="#bdbdbd"/>
        <polygon points="19,0 221,0 221,68 120,100 19,68" fill="#d0d0d0"/>
      </svg>
      <h2>Latest news</h2>
    </div>

    <div class="abs icon" role="img" aria-label="Red and white megaphone illustration" style="left:112px;top:93px"></div>
    <div class="abs icon" role="img" aria-label="Light bulb illustration with red base" style="left:470px;top:88px;width:56px;height:92px"></div>
    <div class="abs icon" role="img" aria-label="Illustration of two people in front of a screen" style="left:782px;top:106px;width:74px;height:58px"></div>

    <p class="abs copy" style="left:16px;top:190px;width:283px">We offer specialised point of sale (POS) support to the hospitality industry. We already support hundreds of cafes and restaurants. We are also about to launch and promote a range of new services with the offering of General IT Support being the most important. Other additional services to be offered are Falcon Cloud Backup, reselling and supporting Korvel Antivirus and Tresby Apps.</p>
    <a class="abs more" href="#" style="left:232px;top:290px">VIEW MORE..</a>

    <div class="abs rule" style="left:352px;top:186px;width:290px"></div>
    <p class="abs copy copy-lg" style="left:363px;top:190px;width:283px">Offers IT solutions for hospitality businesses. In addition to hotels, it offers software for restaurants; golf &amp; spa; leisure Clubs, catering companies, amusement / entertainment facilities, banquets / events, etc.</p>
    <a class="abs more" href="#" style="left:576px;top:283px">VIEW MORE..</a>

    <div class="abs rule" style="left:684px;top:186px;width:268px"></div>
    <div class="abs news" style="left:696px;top:192px;width:262px">
      <h3>Specialised point of sale (POS) support to the hospitality industry.</h3>
      <p>29 Nov 2012</p>
      <h3>Falcon Cloud Backup, reselling and supporting Korvel Antivirus and Tresby Apps.</h3>
      <p>29 Nov 2012</p>
    </div>
    <a class="abs more" href="#" style="left:882px;top:294px">VIEW MORE..</a>
  </section>

  <footer class="abs footer">
    <nav class="abs footer-nav">
      <a href="#" style="margin-right:84px">Home</a>
      <a href="#" style="margin-right:86px">What we are</a>
      <a href="#" style="margin-right:66px">What we offer</a>
      <a href="#">Contact us</a>
    </nav>
    <div class="abs social social-foot" aria-label="Social links"><span></span><span></span><span></span></div>
  </footer>
</div>

<div class="abs copyright">© COPYRIGHT <em>FALCON TECH</em></div>

</body>
</html>
```